Pet Products Label

need a few designs for a line of pet supplements . labels are approx. 3 inch x 11 inches. brand is called Wagtail Works

Target Market(s)

pet owners

Industry/Entity Type

pets supplies

Font styles to use
Sans Serif

Colors
0054AA
0677BA
7BADD7
CADEEF
E8F1F8
FFC000
F8CF3A
FAE287
FDF2CF
FEFAEE

Requirements
Nice to have
• clean logo and easy to read label

```html
<!DOCTYPE html>
<html lang="en">
<head>
<meta charset="utf-8">
<title>Wagtail Works – Daily Gut + Immunity Label</title>
<link rel="stylesheet" href="https://fonts.googleapis.com/css2?family=Montserrat:wght@600;700;800;900&display=swap">
<style>
  :root {
    --backdrop: #E8F1F8;
    --label-yellow: #F8CF3A;
    --label-white: #FFFFFF;
    --brand-blue: #0054AA;
    --accent-blue: #2F62B8;
  }
  html, body {
    margin: 0;
    padding: 0;
    width: 1200px;
    height: 750px;
    overflow: hidden;
    background: var(--backdrop);
  }
  .canvas {
    position: relative;
    width: 1200px;
    height: 750px;
  }
  .label {
    position: absolute;
    left: 170px;
    top: 17px;
    width: 860px;
    height: 716px;
    font-family: "Montserrat", sans-serif;
  }
  .label svg { display: block; }
  .label-bg { fill: var(--label-yellow); }
  .dot { fill: var(--label-white); }
  .brand-mark { fill: var(--accent-blue); }
  .brand-name {
    fill: var(--accent-blue);
    font-weight: 600;
    font-size: 38px;
    letter-spacing: 0.38em;
  }
  .product-title {
    font-weight: 900;
    font-size: 100px;
    letter-spacing: -0.01em;
  }
  .product-title.line-one { fill: var(--brand-blue); }
  .product-title.line-two { fill: var(--accent-blue); }
  .flavor-frame {
    fill: none;
    stroke: var(--brand-blue);
    stroke-width: 2.5;
  }
  .flavor-text {
    fill: var(--accent-blue);
    font-weight: 800;
    font-size: 34px;
    letter-spacing: 0.01em;
  }
  .count-number {
    fill: var(--brand-blue);
    font-weight: 900;
    font-size: 86px;
  }
  .count-unit {
    fill: var(--brand-blue);
    font-weight: 800;
    font-size: 31px;
  }
  .claims {
    fill: var(--brand-blue);
    font-weight: 800;
    font-size: 20px;
  }
</style>
</head>
<body>
<div class="canvas">
  <div class="label">
    <svg width="860" height="716" viewBox="0 0 860 716" xmlns="http://www.w3.org/2000/svg">
      <defs>
        <clipPath id="upper-band"><rect x="0" y="0" width="860" height="353"/></clipPath>
        <clipPath id="label-area"><rect x="0" y="0" width="860" height="716"/></clipPath>
      </defs>

      <rect class="label-bg" x="0" y="0" width="860" height="716"/>

      <g class="dots-upper" clip-path="url(#upper-band)">
        <circle class="dot" cx="213" cy="385" r="146"/>
        <circle class="dot" cx="633" cy="385" r="146"/>
        <circle class="dot" cx="-70" cy="420" r="128"/>
      </g>

      <g class="dots-lower" clip-path="url(#label-area)">
        <circle class="dot" cx="202" cy="751" r="146"/>
        <circle class="dot" cx="644" cy="779" r="146"/>
      </g>

      <circle class="brand-mark" cx="432" cy="106" r="32"/>
      <text class="brand-name" x="436" y="190" text-anchor="middle">WAGTAIL WORKS</text>

      <text class="product-title line-one" x="438" y="364" text-anchor="middle">DAILY GUT+</text>
      <text class="product-title line-two" x="436" y="457" text-anchor="middle">IMMUNITY</text>

      <rect class="flavor-frame" x="218" y="502" width="418" height="45"/>
      <text class="flavor-text" x="427" y="537" text-anchor="middle">CHICKEN FLAVOR</text>

      <text class="count-number" x="52" y="623">30</text>
      <text class="count-unit" x="52" y="661">CHEWS</text>

      <text class="claims" x="809" y="640" text-anchor="end">VET FORMULATED</text>
      <text class="claims" x="809" y="664" text-anchor="end">MADE IN USA</text>
    </svg>
  </div>
</div>
</body>
</html>
```